Business Card for New Business

Please design a business card using our logo and font files. This is only one card for one person, as listed in details section.

Contact Information for Business Card

Dale Vornhuser

Phone 326.815.3926
Cell 459.461.8075
Email dale@morlenbay.com

www.morlenbay.com

Address
31800 Pinecrest Lane #412
Larkfield, PA 18342

Font styles to use
Sans Serif

Requirements
Must have
• Information listed in detail section. Must be standard card size.

```html
<!DOCTYPE html>
<html lang="en">
<head>
<meta charset="utf-8">
<title>Morlenbay Business Card</title>
<link href="https://fonts.googleapis.com/css2?family=Josefin+Sans:wght@300;400;600&display=swap" rel="stylesheet">
<style>
  :root {
    --accent: #e44026;
    --dark: #2b2b2b;
    --dark-glow: #3a3a3a;
    --row: #444444;
    --row-icon: #3a3a3a;
    --paper: #ffffff;
    --ink-light: #f2f2f2;
  }
  * { margin: 0; padding: 0; box-sizing: border-box; }
  html, body { width: 1200px; height: 1200px; overflow: hidden; background: var(--paper); }
  body { position: relative; font-family: "Josefin Sans", sans-serif; }

  .card {
    position: absolute;
    left: 304px;
    width: 592px;
    height: 376px;
    overflow: hidden;
    box-shadow: 3px 5px 6px rgba(0,0,0,0.35);
  }

  /* Front */
  .card-front {
    top: 174px;
    background: radial-gradient(ellipse at 50% 45%, var(--dark-glow) 0%, var(--dark) 65%);
  }
  .front-top-band { position: absolute; left: 0; top: 0; width: 100%; height: 32px; background: var(--accent); }
  .front-bottom-band { position: absolute; left: 0; bottom: 0; width: 100%; height: 33px; }
  .front-web {
    position: absolute; left: 0; width: 100%; bottom: 6px;
    text-align: center; color: var(--accent);
    font-weight: 600; font-size: 25px; letter-spacing: 0.5px;
  }
  .brand {
    position: absolute; left: 0; width: 100%;
    display: flex; align-items: center; justify-content: center; gap: 10px;
  }
  .brand-dot { width: 34px; height: 34px; border-radius: 50%; background: var(--accent); flex: none; }
  .brand-name { font-weight: 300; line-height: 1; white-space: nowrap; }
  .card-front .brand { top: 182px; }
  .card-front .brand-name { font-size: 66px; color: var(--ink-light); }

  /* Back */
  .card-back { top: 650px; background: var(--paper); border: 2px solid var(--dark); }
  .side-tab { position: absolute; left: 0; top: 62px; width: 16px; height: 250px; }
  .logo-panel { position: absolute; left: 16px; top: 0; width: 250px; height: 100%; }
  .card-back .brand { top: 160px; gap: 8px; }
  .card-back .brand-dot { width: 22px; height: 22px; }
  .card-back .brand-name { font-size: 40px; color: var(--accent); }

  .info-panel {
    position: absolute; left: 266px; top: 0; right: 0; bottom: 0;
    background: radial-gradient(ellipse at 50% 30%, var(--dark-glow) 0%, var(--dark) 70%);
  }
  .person-name {
    position: absolute; left: 0; right: 0; top: 38px;
    text-align: center; color: var(--ink-light);
    font-weight: 600; font-size: 29px; line-height: 40px;
  }
  .contact-list { position: absolute; left: 0; right: 0; top: 144px; list-style: none; }
  .contact-row {
    display: flex; align-items: center;
    background: var(--row); border-bottom: 2px solid var(--accent);
  }
  .contact-row:last-child { border-bottom: none; }
  .contact-row.tall { height: 60px; }
  .contact-row.std { height: 42px; }
  .contact-icon {
    width: 38px; align-self: stretch;
    display: flex; align-items: center; justify-content: center;
    background: var(--row-icon);
  }
  .contact-icon svg { width: 26px; height: 26px; display: block; }
  .contact-text {
    padding-left: 14px; color: var(--ink-light);
    font-weight: 300; font-size: 18px; line-height: 22px; white-space: nowrap;
  }
</style>
</head>
<body>

<section class="card card-front">
  <div class="front-top-band"></div>
  <div class="brand">
    <span class="brand-dot"></span>
    <span class="brand-name">morlenbay</span>
  </div>
  <svg class="front-bottom-band" viewBox="0 0 592 33" preserveAspectRatio="none">
    <polygon points="0,0 124,0 157,33 0,33" fill="var(--accent)"/>
    <polygon points="468,0 592,0 592,33 435,33" fill="var(--accent)"/>
  </svg>
  <div class="front-web">www.morlenbay.com</div>
</section>

<section class="card card-back">
  <svg class="side-tab" viewBox="0 0 16 250" preserveAspectRatio="none">
    <polygon points="0,0 16,22 16,228 0,250" fill="var(--accent)"/>
  </svg>
  <div class="logo-panel">
    <div class="brand">
      <span class="brand-dot"></span>
      <span class="brand-name">morlenbay</span>
    </div>
  </div>

  <div class="info-panel">
    <h1 class="person-name">Dale<br>Vornhuser</h1>
    <ul class="contact-list">
      <li class="contact-row tall">
        <span class="contact-icon">
          <svg viewBox="0 0 26 26"><rect width="26" height="26" fill="var(--accent)"/><path d="M5 13 L13 6 L21 13 H18 V20 H14.5 V15.5 H11.5 V20 H8 V13 Z" fill="#fff"/></svg>
        </span>
        <span class="contact-text">31800 Pinecrest Lane #412<br>Larkfield, PA 18342</span>
      </li>
      <li class="contact-row std">
        <span class="contact-icon">
          <svg viewBox="0 0 26 26"><rect width="26" height="26" fill="var(--accent)"/><path d="M8 6 L11 9.5 L9.5 11.5 C10.5 13.8 12.2 15.5 14.5 16.5 L16.5 15 L20 18 L18 20.5 C12 20 6 14 5.5 8 Z" fill="#fff"/></svg>
        </span>
        <span class="contact-text">326.815.3926 - 459.461.8075</span>
      </li>
      <li class="contact-row std">
        <span class="contact-icon">
          <svg viewBox="0 0 26 26"><rect width="26" height="26" fill="var(--accent)"/><path d="M6 7 L20 12 L14 14 L12 20 Z" fill="#fff"/></svg>
        </span>
        <span class="contact-text">dale@morlenbay.com</span>
      </li>
      <li class="contact-row std">
        <span class="contact-icon">
          <svg viewBox="0 0 26 26"><rect width="26" height="26" fill="var(--accent)"/><g fill="none" stroke="#fff" stroke-width="1.4"><circle cx="13" cy="13" r="7"/><ellipse cx="13" cy="13" rx="3" ry="7"/><line x1="6" y1="13" x2="20" y2="13"/><line x1="7" y1="9.5" x2="19" y2="9.5"/><line x1="7" y1="16.5" x2="19" y2="16.5"/></g></svg>
        </span>
        <span class="contact-text">www.morlenbay.com</span>
      </li>
    </ul>
  </div>
</section>

</body>
</html>
```